2 Fold Brochure

We are a spa looking to create a professional elegant two fold brochure for a spa mainly black and white with a splash of lime green.
Look and feel: chic, modern, and spa-ish.

The front will include an image and also it should say: (somewhere under the photo) wherever you think it will look nice.
Skin Tightening
Cellulite Reduction
Body Contouring

The second Page:
Bipolar Radiofrequency(bolded): for immediate face lifting, tone and a complete new younger looking skin!
Multipolar Radiofrequency(bolded): with Vacuum system for body contour, cellulite and fat detachment from adipose tissue.
Cavitation with red LED to treat face and small areas of the body. Red LED light stimulates collagen synthesis.

Ultra Cavitation will sculpt, treat fat, cellulite and improve body shape! It does NOT involve surgery. There is no need for anesthesia, hospital stay or time off from work. Ultra cavitation will promote microscopic air bubbles to surround the lipocyte(fat cell) membranes and with its resonant frequency, the bubbles cause a high enough pressure to break up fat instantly. These broken lipocytes are then safely metabolized out of the human body.

PRESSOTHERAPY: A Complete Body Detox! Pressortherapy based on air pressure, promotes lymphatic drainage. It aslo has infrared system for body heat and electro muscle stimulation system.

Third Page:
Packages:

1. THE NEW FACELIFT:
*Skin Tightening
*Wrinkle Reduction
*Dark Circle Elimination
*Puffy Eye Relief

BODY SHAPING

2. BODY
*Fat Reduction
*Cellulite Reduction
*Body Firming

3. PRESSOTHERAPY (DETOX) $85
*Toxic Flushing
*Lymphatic Drainage
*Toning

5.POST PREGNANCY
*Fat Reduction
*Tummy Firming and Toning
*Cellulite Reduction
*Butt Toning

Buy 5 get 1 Free - $1,250
Buy 10 get 2 Free- $2,500

The back of the second page will include before and after photos I will be sending later. Also include the Logo in the front and by the prices. I have attached our logo.

Also we need a photo to place in the front. Something that shows face and body fat reduction.

Industry/Entity Type

Hospital

```html
<!DOCTYPE html>
<html lang="en">
<head>
<meta charset="utf-8">
<title>What Our Salon Offers</title>
<link rel="stylesheet" href="https://fonts.googleapis.com/css2?family=Source+Sans+3:wght@300;400;600;700&family=Arimo:wght@700&display=swap">
<style>
  :root {
    --lime: #a6ef00;
    --lime-soft: #c4f23a;
    --white: #ffffff;
    --heading-grey: #f2f2f2;
    --shadow: rgba(40, 40, 40, 0.55);
    --photo-green: #b9e28a;
    --photo-olive: #a7a43a;
    --photo-skin: #c0733e;
    --photo-blue: #3f7fd0;
  }
  html, body {
    margin: 0;
    padding: 0;
    overflow: hidden;
    background: var(--white);
  }
  .page {
    position: relative;
    width: 840px;
    height: 1200px;
    overflow: hidden;
    background: var(--lime);
    font-family: "Source Sans 3", sans-serif;
  }
  .page-shapes {
    position: absolute;
    inset: 0;
  }
  .section-title {
    position: absolute;
    margin: 0;
    font-family: "Source Sans 3", sans-serif;
    font-weight: 400;
    font-size: 68px;
    letter-spacing: -0.5px;
    color: var(--heading-grey);
    text-shadow: 2px 3px 4px var(--shadow);
    line-height: 1;
    white-space: nowrap;
  }
  .offers-title { left: 76px; top: 96px; }
  .therapies-title { left: 80px; top: 770px; }
  .offers-list {
    position: absolute;
    left: 80px;
    top: 216px;
    width: 700px;
    color: var(--white);
    font-size: 19px;
    line-height: 28px;
    white-space: nowrap;
  }
  .offers-list p { margin: 0 0 28px; }
  .offers-list strong { font-weight: 700; }
  .therapy-text {
    position: absolute;
    top: 864px;
    margin: 0;
    font-family: "Arimo", sans-serif;
    font-weight: 700;
    font-size: 12.5px;
    line-height: 22px;
    color: var(--white);
    white-space: nowrap;
  }
  .therapy-cavitation { left: 71px; width: 400px; }
  .therapy-presso { left: 507px; width: 230px; }
</style>
</head>
<body>
<main class="page">
  <svg class="page-shapes" width="840" height="1200" viewBox="0 0 840 1200">
    <defs>
      <linearGradient id="photoTone" x1="0" y1="0" x2="1" y2="0.3">
        <stop offset="0" stop-color="var(--photo-green)"/>
        <stop offset="0.45" stop-color="var(--photo-olive)"/>
        <stop offset="0.85" stop-color="var(--photo-skin)"/>
        <stop offset="1" stop-color="#e0a27a"/>
      </linearGradient>
      <radialGradient id="photoBlue" cx="0.92" cy="0.72" r="0.18">
        <stop offset="0" stop-color="var(--photo-blue)" stop-opacity="0.9"/>
        <stop offset="1" stop-color="var(--photo-blue)" stop-opacity="0"/>
      </radialGradient>
      <linearGradient id="limeBand" x1="0" y1="0" x2="1" y2="0">
        <stop offset="0" stop-color="var(--lime-soft)"/>
        <stop offset="1" stop-color="var(--lime)"/>
      </linearGradient>
      <radialGradient id="circleTone" cx="0.3" cy="0.5" r="0.7">
        <stop offset="0" stop-color="#f6d6d6"/>
        <stop offset="1" stop-color="#e49a9a"/>
      </radialGradient>
    </defs>
    <path d="M0,0 H840 V440 C650,620 330,700 0,690 Z" fill="url(#limeBand)"/>
    <g role="img" aria-label="Close-up photo of a facial treatment device on skin in soft green and warm tones">
      <path d="M0,0 H840 V460 C640,620 330,680 0,660 Z" fill="url(#photoTone)"/>
      <path d="M0,0 H840 V460 C640,620 330,680 0,660 Z" fill="url(#photoBlue)"/>
    </g>
    <path d="M0,690 C330,700 650,620 840,440 V640 C600,700 300,750 0,750 Z" fill="var(--white)"/>
    <path d="M0,750 C300,750 600,700 840,640 V1200 H0 Z" fill="var(--lime)"/>
    <path d="M840,1150 C800,1180 760,1195 720,1200 H840 Z" fill="var(--white)"/>
    <circle cx="912" cy="766" r="108" fill="var(--white)"/>
    <circle cx="912" cy="766" r="96" fill="url(#circleTone)" role="img" aria-label="Round photo of a relaxed spa client"/>
  </svg>

  <h1 class="section-title offers-title">what our salon offers</h1>
  <section class="offers-list">
    <p><strong>BIPOLAR RADIOFREQUENCY :</strong> for immediate face lifting, tone and a complete<br>new younger looking skin!</p>
    <p><strong>Multipolar Radiofrequency :</strong> with Vacuum system for body contour, cellulite<br>and fat detachment from adipose tissue.</p>
    <p>Cavitation with red LED to treat face and small areas of the body. Red LED light<br>stimulates collagen synthesis.</p>
  </section>

  <h2 class="section-title therapies-title">other theraputics</h2>
  <p class="therapy-text therapy-cavitation">Ultra Cavitation will sculpt, treat fat, cellulite and improve body<br>shape! It does NOT involve surgery. There is no need for<br>anesthesia, hospital stay or time off from work. Ultra cavitation<br>will promote microscopic air bubbles to surround the<br>lipocyte(fat cell) membranes and with its resonant<br>frequency, the bubbles cause a high enough pressure to break<br>up fat instantly. These broken lipocytes are then safely<br>metabolized out of the human body.</p>
  <p class="therapy-text therapy-presso">PRESSOTHERAPY: A Complete<br>Body Detox! Pressortherapy based<br>on air pressure, promotes lymphatic<br>drainage. It aslo has infrared system<br>for body heat and electro muscle<br>stimulation system.</p>
</main>
</body>
</html>
```